Business card design needed

New company based in Brisbane, Australia. Brindle Systems. The business is focused on the delivery of network architecture design and deployment. We will provide both services and the sale of the necessary equipment to deliver the service. Cloud computing is an important element of our focus as this is an emerging market for enterprises in Queensland. Our target marketplace is medium to large corporations with complex infrastructure requirements. IT Management and above will be the typical entry point for us into these accounts. We would like to see the use of various shade of green, design should be clutter free and impress stability, trust and growth.
Updates
Hey Everyone
Just we let you all know we have changed this project to 'committed' payment status.
Looking forward to seeing the designs! Thanks for your efforts.
Best Regards
Marcus
Industry/Entity Type
Architecture
Contact Information for Business Card
Brindle Systems, Marcus Doyle, Sales Director, Level 14 Harlow Tower, 58 Penfold Street, Brisbane QLD 4000, Ph +61 7 3904 2267, M +61 4 4926 1573, E marcus.doyle@brindlesystems-example.com.au
Look and feel
Each slider illustrates characteristics of the customer's brand and the style your logo design should communicate.

```html
<!DOCTYPE html>
<html lang="en">
<head>
<meta charset="utf-8">
<title>Brindle Systems – Business Cards</title>
<link href="https://fonts.googleapis.com/css2?family=Didact+Gothic&display=swap" rel="stylesheet">
<style>
  :root {
    --page-bg: #eeeeee;
    --card-dark: #173d1e;
    --card-mid: #235a2d;
    --card-light: #2d6a37;
    --band: rgba(255, 255, 255, 0.07);
    --band-strong: rgba(255, 255, 255, 0.10);
    --text-main: #f4f7f2;
    --text-muted: #7f9e84;
    --watermark: rgba(255, 255, 255, 0.05);
  }
  * { margin: 0; padding: 0; box-sizing: border-box; }
  html, body {
    width: 1200px;
    height: 1009px;
    overflow: hidden;
    background: var(--page-bg);
    font-family: "Didact Gothic", "Helvetica Neue", Arial, sans-serif;
    color: var(--text-main);
  }
  .canvas { position: relative; width: 1200px; height: 1009px; }

  .card {
    position: absolute;
    width: 650px;
    height: 361px;
    overflow: hidden;
    background: linear-gradient(160deg, var(--card-dark) 0%, var(--card-mid) 55%, var(--card-light) 100%);
    box-shadow: 0 6px 18px rgba(0, 0, 0, 0.25);
  }
  .card-landscape { left: 150px; top: 110px; }
  .card-portrait-name { left: 400px; top: 545px; }

  .band { position: absolute; left: 0; width: 100%; }
  .text { position: absolute; white-space: nowrap; letter-spacing: 0.04em; }

  .company { font-size: 38px; }
  .person-name { font-size: 36px; }
  .job-title { font-size: 20px; color: var(--text-muted); }
  .contact-line { font-size: 21px; line-height: 37px; }
  .address { font-size: 23px; line-height: 40px; }
  .email { font-size: 22px; }
  .label { display: inline-block; width: 32px; }

  /* Card one */
  .card-landscape .band-main { top: 148px; height: 150px; background: var(--band); }
  .card-landscape .band-email { top: 298px; height: 63px; background: var(--band-strong); }
  .card-landscape .company { right: 42px; top: 34px; }
  .card-landscape .person-name { left: 36px; top: 100px; }
  .card-landscape .job-title { left: 40px; top: 152px; }
  .card-landscape .phones { left: 40px; top: 205px; }
  .card-landscape .address { left: 345px; top: 142px; }
  .card-landscape .email { left: 40px; top: 312px; }

  /* Card two */
  .card-portrait-name .watermark {
    color: var(--watermark);
    font-size: 46px;
    line-height: 68px;
  }
  .card-portrait-name .band-email { top: 295px; height: 50px; background: var(--band-strong); }
  .card-portrait-name .person-name { left: 42px; top: 40px; }
  .card-portrait-name .job-title { left: 46px; top: 92px; }
  .card-portrait-name .phones { left: 46px; top: 165px; }
  .card-portrait-name .company-block { left: 330px; top: 135px; }
  .card-portrait-name .company-block .company { font-size: 26px; display: block; line-height: 38px; }
  .card-portrait-name .email { left: 42px; top: 305px; }
</style>
</head>
<body>
<main class="canvas">

  <section class="card card-landscape" aria-label="Business card, layout one">
    <div class="band band-main"></div>
    <div class="band band-email"></div>
    <div class="text company">Brindle Systems</div>
    <div class="text person-name">Marcus Doyle</div>
    <div class="text job-title">Sales Director</div>
    <div class="text contact-line phones">
      <div><span class="label">Ph</span>+61 7 3904 2267</div>
      <div><span class="label">M</span>+61 4 4926 1573</div>
    </div>
    <div class="text address">
      <div>Level 14 Harlow Tower</div>
      <div>58 Penfold Street</div>
      <div>Brisbane QLD 4000</div>
    </div>
    <div class="text email"><span class="label">E</span>marcus.doyle@brindlesystems-example.com.au</div>
  </section>

  <section class="card card-portrait-name" aria-label="Business card, layout two">
    <div class="text watermark" style="left: 150px; top: 20px;" aria-hidden="true">Brindle Systems</div>
    <div class="text watermark" style="left: -20px; top: 115px;" aria-hidden="true">Brindle Systems</div>
    <div class="band band-email"></div>
    <div class="text person-name">Marcus Doyle</div>
    <div class="text job-title">Sales Director</div>
    <div class="text contact-line phones">
      <div><span class="label">Ph</span>+61 7 3904 2267</div>
      <div><span class="label">M</span>+61 4 4926 1573</div>
    </div>
    <div class="text address company-block">
      <span class="company">Brindle Systems</span>
      <div>Level 14 Harlow Tower</div>
      <div>58 Penfold Street</div>
      <div>Brisbane QLD 4000</div>
    </div>
    <div class="text email"><span class="label">E</span>marcus.doyle@brindlesystems-example.com.au</div>
  </section>

</main>
</body>
</html>
```